Flyer for Car Detailing Shop

I am opening a detailing shop. I am looking for a nice, easy to read single sided flyer I can hand out at car shows, hang in store windows and to my clients and customers to promote my business. I want it a little professional yet attention grabbing. I want someone to look at it and go "holy shit, thats a nice flyer" haha

Here are some things that must be included:
- Company Name: Falconridge Motorworks Detailing & Coatings
- Tag Line: Shine Beyond Measure
- Address: 4815 Harwick Rd, Alder Bay, MI 48990
- www.falconridgemotorworks.example
- Find Us on social Media! ::insert facebook and instagram logo
Colors: Black, Lime Green and Purple for accents, etc

HAND WASH
- Express Wash start at $25
- Deluxe Wash Start at $50

EXTERIOR DETAILING
-Basic Packages Start at $160
- Deluxe Packages Start at $350

INTERIOR DETAILING
- Basic Packages Start at $60
- Deluxe Packages Start at $200

New Car Prep and Ceramic Coatings
*Consultation required prior to beginning work*
- Paint: Starting at $500
- Interior: Starting at $100
- Wheels Off: Starting at $200
- Trim: Starting at $100
- Windows: $50 windshield/ $25 per pane

Additional Services
- Scratch removal
- Ozone Treatment
- Headlight Restoration
- Chip Repair

```html
<!DOCTYPE html>
<html lang="en">
<head>
<meta charset="utf-8">
<title>Falconridge Motorworks – Flyer</title>
<link rel="stylesheet" href="https://fonts.googleapis.com/css2?family=Poppins:wght@800&family=Raleway:wght@500;600;700;800&display=swap">
<style>
  :root {
    --white: #ffffff;
    --ink: #1b1b1b;
    --charcoal: #2f2f2f;
    --graphite: #454545;
    --lime: #6cc04a;
    --leaf: #3f8f2c;
    --purple: #5a1e8c;
    --purple-deep: #3d1466;
    --line: #8fd06f;
    --text-light: #f2f2f2;
  }
  * { margin: 0; padding: 0; box-sizing: border-box; }
  html, body { width: 720px; height: 1200px; overflow: hidden; background: var(--white); }
  .flyer {
    position: relative; width: 720px; height: 1200px; overflow: hidden;
    font-family: "Raleway", Arial, sans-serif; color: var(--ink);
  }
  .backdrop { position: absolute; inset: 0; }
  .abs { position: absolute; }

  .brand {
    left: 24px; top: 150px; width: 230px; text-align: center;
    font-weight: 800; font-size: 27px; line-height: 1.12; color: var(--ink);
  }
  .brand-dot { left: 112px; top: 70px; width: 56px; height: 56px; border-radius: 50%; background: var(--ink); }

  .tagline { font-family: "Poppins", sans-serif; font-weight: 800; line-height: 1; letter-spacing: -1px; white-space: nowrap; }
  .tagline-1 { left: 30px; top: 344px; font-size: 62px; color: var(--white); }
  .tagline-2 { left: 110px; top: 418px; font-size: 62px; color: var(--lime); }

  .heading { font-weight: 800; font-size: 21px; color: var(--purple); line-height: 1.1; text-transform: uppercase; white-space: nowrap; }
  .heading.on-dark { color: var(--lime); }
  .rule { height: 3px; background: var(--line); }

  .row { display: flex; align-items: center; font-size: 16.5px; font-weight: 500; white-space: nowrap; }
  .row .tick { width: 14px; height: 14px; margin-right: 12px; flex: none; }
  .row .price { position: absolute; }
  .row.on-dark { color: var(--text-light); }
  .label { color: var(--leaf); }

  .note { left: 32px; top: 808px; font-size: 16.5px; font-weight: 700; line-height: 1.35; }

  .pill {
    left: 392px; top: 872px; padding: 3px 14px; border-radius: 18px;
    background: var(--lime); color: var(--ink); font-weight: 800; font-size: 20px; white-space: nowrap;
  }
  .extra { display: flex; align-items: center; font-size: 21px; font-weight: 500; color: var(--text-light); white-space: nowrap; }
  .extra .bullet { width: 26px; height: 26px; border-radius: 50%; background: var(--lime); margin-right: 16px; flex: none; }

  .contact { display: flex; align-items: center; font-size: 22px; font-weight: 500; color: var(--white); white-space: nowrap; }
  .contact svg { width: 24px; height: 24px; margin-right: 22px; flex: none; }

  .social-cta {
    left: 480px; top: 1075px; width: 210px; height: 32px; border-radius: 14px 0 0 0;
    background: var(--lime); color: var(--ink); font-weight: 700; font-size: 15.5px;
    display: flex; align-items: center; justify-content: center; white-space: nowrap;
  }
  .social-dot { width: 44px; height: 44px; border-radius: 50%; }
  .social-a { left: 581px; top: 1131px; background: #3b5ba8; }
  .social-b { left: 637px; top: 1131px; background: #d8407a; }
</style>
</head>
<body>
<main class="flyer">
  <svg class="backdrop" width="720" height="1200" viewBox="0 0 720 1200" aria-hidden="true">
    <defs>
      <linearGradient id="photoTone" x1="0" y1="0" x2="1" y2="1">
        <stop offset="0" stop-color="#3a3a40"/>
        <stop offset="0.45" stop-color="#15182a"/>
        <stop offset="0.75" stop-color="#2a1a1c"/>
        <stop offset="1" stop-color="#0c0d12"/>
      </linearGradient>
      <linearGradient id="panelTone" x1="0" y1="0" x2="1" y2="0">
        <stop offset="0" stop-color="#3b3b3b"/>
        <stop offset="0.6" stop-color="#343434" stop-opacity="0.92"/>
        <stop offset="1" stop-color="#222" stop-opacity="0.4"/>
      </linearGradient>
      <linearGradient id="columnTone" x1="0" y1="0" x2="0" y2="1">
        <stop offset="0" stop-color="#4a4a4a"/>
        <stop offset="1" stop-color="#222"/>
      </linearGradient>
      <linearGradient id="footerTone" x1="0" y1="0" x2="1" y2="0">
        <stop offset="0" stop-color="#3d1466"/>
        <stop offset="1" stop-color="#6a2aa0"/>
      </linearGradient>
    </defs>
    <polygon points="334,0 362,0 252,282 222,282" fill="var(--lime)"/>
    <g role="img" aria-label="Photo: detailer in a respirator machine-polishing a dark car at night">
      <polygon points="360,0 720,0 720,620 250,282" fill="url(#photoTone)"/>
    </g>
    <polygon points="0,350 250,280 720,400 720,612 0,497" fill="url(#panelTone)"/>
    <polygon points="356,560 720,614 720,1200 356,1200" fill="url(#columnTone)"/>
    <polygon points="0,492 720,604 720,620 0,534" fill="var(--lime)"/>
    <polygon points="0,1078 440,1078 580,1200 0,1200" fill="url(#footerTone)"/>
  </svg>

  <div class="abs brand-dot"></div>
  <div class="abs brand">Falconridge Motorworks Detailing &amp; Coatings</div>

  <div class="abs tagline tagline-1">Shine Beyond</div>
  <div class="abs tagline tagline-2">Measure</div>

  <!-- Hand wash -->
  <div class="abs heading" style="left:32px;top:571px;">Hand Wash</div>
  <div class="abs rule" style="left:32px;top:604px;width:296px;"></div>
  <div class="abs row" style="left:32px;top:622px;width:300px;">
    <svg class="tick" viewBox="0 0 14 14"><circle cx="7" cy="7" r="6" fill="none" stroke="var(--purple)" stroke-width="1.4"/><path d="M4 7l2 2 4-4" fill="none" stroke="var(--purple)" stroke-width="1.4"/></svg>
    Express Wash start at<span class="price" style="left:256px;">$25</span></div>
  <div class="abs row" style="left:32px;top:656px;width:300px;">
    <svg class="tick" viewBox="0 0 14 14"><circle cx="7" cy="7" r="6" fill="none" stroke="var(--purple)" stroke-width="1.4"/><path d="M4 7l2 2 4-4" fill="none" stroke="var(--purple)" stroke-width="1.4"/></svg>
    Deluxe Wash Start at<span class="price" style="left:256px;">$50</span></div>

  <!-- New car prep -->
  <div class="abs heading" style="left:32px;top:729px;">New Car Prep<br>and Ceramic Coatings</div>
  <div class="abs rule" style="left:32px;top:789px;width:296px;"></div>
  <div class="abs note">Consultation required prior to<br>beginning work</div>
  <div class="abs" style="left:32px;top:870px;width:300px;">
    <div class="row" style="position:relative;height:31px;"><svg class="tick" viewBox="0 0 14 14"><circle cx="7" cy="7" r="6" fill="none" stroke="var(--purple)" stroke-width="1.4"/><path d="M4 7l2 2 4-4" fill="none" stroke="var(--purple)" stroke-width="1.4"/></svg><span class="label">Paint:</span>&nbsp;Starting at<span class="price" style="left:256px;">$500</span></div>
    <div class="row" style="position:relative;height:31px;"><svg class="tick" viewBox="0 0 14 14"><circle cx="7" cy="7" r="6" fill="none" stroke="var(--purple)" stroke-width="1.4"/><path d="M4 7l2 2 4-4" fill="none" stroke="var(--purple)" stroke-width="1.4"/></svg><span class="label">Interior:</span>&nbsp;Starting at<span class="price" style="left:256px;">$100</span></div>
    <div class="row" style="position:relative;height:31px;"><svg class="tick" viewBox="0 0 14 14"><circle cx="7" cy="7" r="6" fill="none" stroke="var(--purple)" stroke-width="1.4"/><path d="M4 7l2 2 4-4" fill="none" stroke="var(--purple)" stroke-width="1.4"/></svg><span class="label">Wheels Off:</span>&nbsp;Starting at<span class="price" style="left:256px;">$200</span></div>
    <div class="row" style="position:relative;height:31px;"><svg class="tick" viewBox="0 0 14 14"><circle cx="7" cy="7" r="6" fill="none" stroke="var(--purple)" stroke-width="1.4"/><path d="M4 7l2 2 4-4" fill="none" stroke="var(--purple)" stroke-width="1.4"/></svg><span class="label">Trim:</span>&nbsp;Starting at<span class="price" style="left:256px;">$100</span></div>
    <div class="row" style="position:relative;height:31px;"><svg class="tick" viewBox="0 0 14 14"><circle cx="7" cy="7" r="6" fill="none" stroke="var(--purple)" stroke-width="1.4"/><path d="M4 7l2 2 4-4" fill="none" stroke="var(--purple)" stroke-width="1.4"/></svg><span class="label">Windows</span>&nbsp;at<span class="price" style="left:256px;">$50</span></div>
    <div class="row" style="position:relative;height:31px;"><svg class="tick" viewBox="0 0 14 14"><circle cx="7" cy="7" r="6" fill="none" stroke="var(--purple)" stroke-width="1.4"/><path d="M4 7l2 2 4-4" fill="none" stroke="var(--purple)" stroke-width="1.4"/></svg><span class="label">windshield</span>&nbsp;per pane at<span class="price" style="left:256px;">$25</span></div>
  </div>

  <!-- Exterior -->
  <div class="abs heading on-dark" style="left:392px;top:614px;">Exterior Detailing</div>
  <div class="abs rule" style="left:392px;top:645px;width:294px;"></div>
  <div class="abs row on-dark" style="left:392px;top:666px;width:300px;"><svg class="tick" viewBox="0 0 14 14"><circle cx="7" cy="7" r="6" fill="none" stroke="var(--lime)" stroke-width="1.4"/><path d="M4 7l2 2 4-4" fill="none" stroke="var(--lime)" stroke-width="1.4"/></svg>Basic Packages Start at<span class="price" style="left:258px;">$160</span></div>
  <div class="abs row on-dark" style="left:392px;top:690px;width:300px;"><svg class="tick" viewBox="0 0 14 14"><circle cx="7" cy="7" r="6" fill="none" stroke="var(--lime)" stroke-width="1.4"/><path d="M4 7l2 2 4-4" fill="none" stroke="var(--lime)" stroke-width="1.4"/></svg>Deluxe Packages Start at<span class="price" style="left:258px;">$350</span></div>

  <!-- Interior -->
  <div class="abs heading on-dark" style="left:392px;top:752px;">Interior Detailing</div>
  <div class="abs rule" style="left:392px;top:783px;width:294px;"></div>
  <div class="abs row on-dark" style="left:392px;top:800px;width:300px;"><svg class="tick" viewBox="0 0 14 14"><circle cx="7" cy="7" r="6" fill="none" stroke="var(--lime)" stroke-width="1.4"/><path d="M4 7l2 2 4-4" fill="none" stroke="var(--lime)" stroke-width="1.4"/></svg>Basic Packages Start at<span class="price" style="left:258px;">$60</span></div>
  <div class="abs row on-dark" style="left:392px;top:827px;width:300px;"><svg class="tick" viewBox="0 0 14 14"><circle cx="7" cy="7" r="6" fill="none" stroke="var(--lime)" stroke-width="1.4"/><path d="M4 7l2 2 4-4" fill="none" stroke="var(--lime)" stroke-width="1.4"/></svg>Deluxe Packages Start at<span class="price" style="left:258px;">$200</span></div>

  <!-- Additional services -->
  <div class="abs pill">ADDITIONAL SERVICES</div>
  <div class="abs" style="left:394px;top:918px;">
    <div class="extra" style="height:32px;"><span class="bullet"></span>Scratch removal</div>
    <div class="extra" style="height:32px;"><span class="bullet"></span>Ozone Treatment</div>
    <div class="extra" style="height:32px;"><span class="bullet"></span>Headlight Restoration</div>
    <div class="extra" style="height:36px;"><span class="bullet"></span>Chip Repair</div>
  </div>

  <!-- Footer -->
  <div class="abs" style="left:30px;top:1083px;">
    <div class="contact" style="height:36px;">
      <svg viewBox="0 0 24 24"><circle cx="12" cy="12" r="12" fill="var(--lime)"/><rect x="6" y="8" width="12" height="8" fill="var(--purple-deep)"/><path d="M6 8l6 5 6-5" fill="none" stroke="var(--lime)" stroke-width="1.2"/></svg>
      info@falconridge.example</div>
    <div class="contact" style="height:36px;">
      <svg viewBox="0 0 24 24"><circle cx="12" cy="12" r="12" fill="var(--lime)"/><circle cx="12" cy="12" r="6" fill="none" stroke="var(--purple-deep)" stroke-width="1.4"/><path d="M6 12h12M12 6v12" stroke="var(--purple-deep)" stroke-width="1.2"/></svg>
      www.falconridgemotorworks.example</div>
    <div class="contact" style="height:36px;">
      <svg viewBox="0 0 24 24"><circle cx="12" cy="12" r="12" fill="var(--lime)"/><path d="M12 19c-3-4-5-6-5-9a5 5 0 0110 0c0 3-2 5-5 9z" fill="var(--purple-deep)"/><circle cx="12" cy="10" r="1.8" fill="var(--lime)"/></svg>
      4815 Harwick Rd, Alder Bay, MI 48990</div>
  </div>

  <div class="abs social-cta">Find Us on social Media!</div>
  <div class="abs social-dot social-a"></div>
  <div class="abs social-dot social-b"></div>
</main>
</body>
</html>
```